Letterhead, business card and email signature design

I have a new company and I would like a professional letterhead, business card and email signature designed. Id like the business card to have room for a photo of the bearer. I'd also like the template to be editable so we can adapt for future members of staff etc.

```html
<!DOCTYPE html>
<html lang="en">
<head>
<meta charset="utf-8">
<title>Nimbus Links – Stationery Set</title>
<link rel="stylesheet" href="https://fonts.googleapis.com/css2?family=Lato:wght@400;700&display=swap">
<style>
  :root{
    --backdrop:#cdc2ae;
    --paper:#ffffff;
    --navy:#1c3258;
    --magenta:#a81d58;
    --ink:#5f5f63;
    --ink-soft:#7a7a7e;
    --rule:#4a4a4e;
  }
  *{box-sizing:border-box;margin:0;padding:0}
  html,body{width:1200px;height:1200px;overflow:hidden}
  body{background:var(--backdrop);font-family:"Lato",sans-serif;color:var(--ink);position:relative}

  .sheet{position:absolute;background:var(--paper);box-shadow:0 8px 14px rgba(0,0,0,.18)}

  /* brand lockup */
  .brand{position:absolute;display:flex;align-items:center;gap:6px}
  .brand__dot{border-radius:50%;background:var(--navy);flex:none}
  .brand__name{font-family:"Lato",sans-serif;font-weight:700;color:var(--navy);letter-spacing:.04em;white-space:nowrap}

  /* letterhead */
  .letterhead{left:252px;top:111px;width:545px;height:775px}
  .letterhead .brand{left:36px;top:63px}
  .letterhead .brand__dot{width:54px;height:54px}
  .letterhead .brand__name{font-size:16px}
  .lh-contact{position:absolute;left:442px;top:67px;list-style:none;font-size:5px;line-height:10.5px;color:var(--ink-soft)}
  .lh-contact li{display:flex;align-items:center;gap:6px}
  .icon{fill:var(--magenta);flex:none}
  .letter{position:absolute;left:36px;top:185px;width:477px;font-size:9px;line-height:11.1px}
  .letter__date{font-weight:700;font-size:9.4px;margin-bottom:8px}
  .letter__recipient{font-size:9.2px;line-height:11.2px;letter-spacing:.03em}
  .letter__recipient p+p{margin-top:4px}
  .letter__greeting{font-weight:700;font-size:9.4px;margin-top:57px}
  .letter__body p{text-align:justify;letter-spacing:.02em}
  .letter__body p:first-child{margin-top:26px}
  .letter__body p+p{margin-top:22px}
  .letter__body p:last-child{margin-top:11px}
  .letter__closing{margin-top:22px;font-size:9.2px;line-height:12px}
  .letter__closing strong{font-weight:700}
  .signature{position:absolute;left:36px;top:553px;width:148px;height:40px;background:linear-gradient(90deg,rgba(40,40,140,.12),rgba(40,40,140,.04));border-bottom:1px solid #9a9aa4}

  /* card front */
  .card-front{left:775px;top:353px;width:249px;height:142px}
  .card-front .brand{left:50%;top:50%;transform:translate(-50%,-50%)}
  .card-front .brand__dot{width:45px;height:45px}
  .card-front .brand__name{font-size:14px}

  /* card back */
  .card-back{left:775px;top:517px;width:249px;height:141px}
  .card-back .brand{left:24px;top:27px;gap:4px}
  .card-back .brand__dot{width:27px;height:27px}
  .card-back .brand__name{font-size:8px}
  .card-back__name{position:absolute;left:24px;top:67px;font-size:7px;font-weight:700;color:var(--navy)}
  .card-back__role{position:absolute;left:25px;top:77px;font-size:4px;color:var(--magenta)}
  .card-back__contact{position:absolute;left:23px;top:96px;list-style:none;font-size:5px;line-height:9px;color:var(--ink-soft)}
  .card-back__contact li{display:flex;align-items:center;gap:4px}
  .trace-fill{position:absolute;background:linear-gradient(135deg,rgba(201,90,138,.35),rgba(82,96,126,.30) 55%,rgba(201,90,138,.25))}
  .card-back .trace-fill{left:153px;top:14px;width:96px;height:109px}

  /* email signature */
  .email-sig{left:249px;top:917px;width:549px;height:127px}
  .email-sig .brand{left:19px;top:20px;gap:5px}
  .email-sig .brand__dot{width:44px;height:44px}
  .email-sig .brand__name{font-size:11px}
  .socials{position:absolute;left:25px;top:83px;display:flex;gap:3px;list-style:none}
  .socials li{width:22px;height:22px;border-radius:50%;background:var(--magenta)}
  .email-sig__name{position:absolute;left:171px;top:15px;font-size:19px;font-weight:700;color:var(--navy);line-height:22px}
  .email-sig__role{position:absolute;left:172px;top:38px;font-size:10px;font-weight:700;color:var(--magenta);line-height:12px}
  .email-sig__rule{position:absolute;left:171px;top:53px;width:235px;height:1px;background:var(--rule)}
  .email-sig__contact{position:absolute;left:170px;top:62px;list-style:none;font-size:10px;line-height:17.5px;color:var(--ink)}
  .email-sig__contact li{display:flex;align-items:center;gap:6px}
  .email-sig__contact .pair span+svg{margin-left:4px}
  .email-sig .trace-fill{left:437px;top:0;width:112px;height:127px}
</style>
</head>
<body>

<section class="sheet letterhead">
  <div class="brand"><span class="brand__dot"></span><span class="brand__name">NIMBUS LINKS</span></div>
  <ul class="lh-contact">
    <li><svg class="icon" width="5" height="5" viewBox="0 0 10 10"><path d="M1 4c2-3 6-3 8 0l-2 1-1-1H4L3 5z M2 6h6v3H2z"/></svg>(+012) 345 678 9</li>
    <li><svg class="icon" width="5" height="5" viewBox="0 0 10 10"><path d="M2 0l2 2-1 2c1 2 2 3 3 3l2-1 2 2-2 2C4 10 0 6 0 2z"/></svg>(+012) 345 678 9</li>
    <li><svg class="icon" width="5" height="5" viewBox="0 0 10 8"><path d="M0 0h10v8H0z M1 1l4 3 4-3" fill="none" stroke="#a81d58" stroke-width="1.4"/></svg>info@nimbuslinks.com</li>
    <li><svg class="icon" width="5" height="5" viewBox="0 0 10 10"><circle cx="5" cy="5" r="4.3" fill="none" stroke="#a81d58" stroke-width="1.2"/><path d="M1 5h8M5 1v8" stroke="#a81d58" stroke-width="1"/></svg>www.nimbuslinks.com</li>
  </ul>

  <article class="letter">
    <p class="letter__date">DATE:3/5/2018</p>
    <div class="letter__recipient">
      <p>Recipient`s name</p>
      <p>14 Meadowbrook Court<br>Fairhaven, OR 97120</p>
    </div>
    <p class="letter__greeting">Dear, Mr________</p>
    <div class="letter__body">
      <p>Lorem ipsum dolor sit amet, consectetur adipiscing elit, sed do eiusmod tempor incididunt ut labore et dolore magna aliqua. Est pellentesque elit ullamcorper dignissim cras.</p>
      <p>Lorem ipsum dolor sit amet, consectetur adipiscing elit, sed do eiusmod tempor incididunt ut labore et dolore magna aliqua. Pharetra et ultrices neque ornare aenean euismod. Nunc eget lorem dolor sed viverra ipsum nunc. Ac ut consequat semper viverra nam libero. Eget gravida cum sociis natoque. Pretium viverra suspendisse potenti nullam. In hendrerit gravida rutrum quisque non. Ultrices gravida dictum fusce ut placerat orci. Accumsan tortor posuere ac ut consequat semper viverra. Feugiat sed lectus vestibulum mattis.</p>
      <p>Lorem ipsum dolor sit amet, consectetur adipiscing elit, sed do eiusmod tempor incididunt ut labore et dolore magna aliqua. Non arcu risus quis varius quam quisque. Tincidunt eget nullam non nisi est sit amet. Tincidunt tortor aliquam nulla facilisi cras fermentum odio eu feugiat. Id leo in vitae turpis massa sed elementum tempus egestas.</p>
    </div>
    <p class="letter__closing"><strong>Your Sincerely</strong><br>M.J Alan Carter</p>
  </article>
  <div class="signature" role="img" aria-label="Handwritten signature"></div>
</section>

<section class="sheet card-front">
  <div class="brand"><span class="brand__dot"></span><span class="brand__name">NIMBUS LINKS</span></div>
</section>

<section class="sheet card-back">
  <div class="brand"><span class="brand__dot"></span><span class="brand__name">NIMBUS LINKS</span></div>
  <p class="card-back__name">Your Name</p>
  <p class="card-back__role">Designation</p>
  <ul class="card-back__contact">
    <li><svg class="icon" width="4" height="4" viewBox="0 0 10 10"><path d="M2 0l2 2-1 2c1 2 2 3 3 3l2-1 2 2-2 2C4 10 0 6 0 2z"/></svg>(+012) 345 678 9</li>
    <li><svg class="icon" width="4" height="4" viewBox="0 0 10 8"><path d="M0 0h10v8H0z"/></svg>info@nimbuslinks.com</li>
    <li><svg class="icon" width="4" height="4" viewBox="0 0 10 10"><circle cx="5" cy="5" r="5"/></svg>www.nimbuslinks.com</li>
  </ul>
  <div class="trace-fill" role="img" aria-label="Decorative circuit-trace pattern in pink and navy lines"></div>
</section>

<section class="sheet email-sig">
  <div class="brand"><span class="brand__dot"></span><span class="brand__name">NIMBUS LINKS</span></div>
  <ul class="socials" aria-label="Social profiles">
    <li></li><li></li><li></li><li></li>
  </ul>
  <p class="email-sig__name">Your Name</p>
  <p class="email-sig__role">Designation</p>
  <div class="email-sig__rule"></div>
  <ul class="email-sig__contact">
    <li class="pair">
      <svg class="icon" width="9" height="9" viewBox="0 0 10 10"><path d="M2 0l2 2-1 2c1 2 2 3 3 3l2-1 2 2-2 2C4 10 0 6 0 2z"/></svg><span>(+012) 345 678 9</span>
      <svg class="icon" width="11" height="8" viewBox="0 0 10 8"><path d="M0 0h10v8H0z"/><path d="M0 0l5 4 5-4" fill="none" stroke="#fff" stroke-width="1"/></svg><span>info@nimbuslinks.com</span>
    </li>
    <li><svg class="icon" width="9" height="11" viewBox="0 0 10 12"><path d="M5 0a4 4 0 0 1 4 4c0 3-4 8-4 8S1 7 1 4a4 4 0 0 1 4-4z"/><circle cx="5" cy="4" r="1.6" fill="#fff"/></svg>88 Willow Street Lakeford, TX 75410</li>
    <li><svg class="icon" width="10" height="10" viewBox="0 0 10 10"><circle cx="5" cy="5" r="4.3" fill="none" stroke="#a81d58" stroke-width="1.2"/><path d="M1 5h8M5 1v8" stroke="#a81d58" stroke-width="1"/></svg>www.nimbuslinks.com</li>
  </ul>
  <div class="trace-fill" role="img" aria-label="Decorative circuit-trace pattern in pink and navy lines"></div>
</section>

</body>
</html>
```